Business Card Needed for Crafter of Pottery, Jewelry and Artwork

Calling all designers in search of an artistic challenge.

I need a new business card design for my pottery, jewelry and artwork business, Woven Glass and Tide, based in Vancouver BC.

I would like a card that is bright and inviting and preferably incorporates my logo and a sample of photos of my work while having a clean fresh look. The following contact details would preferably be included on the card as well:
• Helena Pikeworth
• Designer
• Phone: 604.555.0172
• Email: Designer@WovenGlassandTide.example
• Website: www.WovenGlassandTide.example
• Blog: www.ShapingHillside.example

The logo is attached in two color schemes in both Vector and Source formats. On past cards I’ve also included photos of my work. By including photos of the work the pieces are showcased and it catches people’s eye and prompts them to pick up the card and look at it more closely. For example, if I leave a stack in a coffee shop I want people to be drawn to the card, to pick it up and get a sense of the my product lines. Please feel free to pull photos of my work directly off of my website. If you need photos with higher pixels please let me know and I’ll email them directly to you. The website background is bffbda (191, 251, 218). I would like the business cards to match the feel of the website for consistency but the cards do not need to use the exact same colors. My website and current business card are predominantly turquoise shades. The background uses stripes provided by the website template. I don’t know the exact colors of the stripes.

My current business card is attached to show the use of photos in a design. Please note that I am not thrilled with my own design and am looking for variations and completely new designs. This example is not meant to be used as a template or starting point.

Here is some background surrounding my company:
WGT offers one of a kind jewelry, pottery, artwork and leather bags each designed with a twist. The pottery varies from rustic every day functional ware to raku artwork. The jewelry ranges from simple sterling every day pieces to multimedia pieces incorporating stone, metal, ceramics and fabric. The artwork is multimedia, typically acrylic paired with a natural element such as bark. All the bags are leather with reworked kimono fabric or patterned silk lining.

Feel free to check out my website to get a flavour for my work and the color scheme I've used on marketing materials so far. www.wovenglassandtide.example
Updates

Thank you to everyone who has submitted a design so far. I hope everyone has received some helpful feedback.

I'm going to post a survey to customers and friends asking for their votes. If you have new designs to submit please try to get them in by Saturday March 30 at noon so that I can include it in the survey launch.

Thank you

Target Market(s)

Females aged 25-65 interested in one of a kind functional pottery and jewelry.

Industry/Entity Type

Coffee Shop

Requirements
Must have
• Contact information, website, blog
Nice to have
• Logo, photos

```html
<!DOCTYPE html>
<html lang="en">
<head>
<meta charset="utf-8">
<title>Woven Glass and Tide – Business Card</title>
<link rel="stylesheet" href="https://fonts.googleapis.com/css2?family=EB+Garamond:wght@500;700&display=swap">
<style>
  :root {
    --cream: #e1d9bc;
    --teal: #05b6aa;
    --teal-soft: #3fc4b8;
    --navy: #2b2466;
    --page: #ffffff;
    --shadow: rgba(0, 0, 0, 0.65);
  }
  * { box-sizing: border-box; margin: 0; padding: 0; }
  html, body { width: 1200px; height: 900px; overflow: hidden; background: var(--page); }
  body { position: relative; font-family: "EB Garamond", Georgia, serif; color: var(--navy); }

  .card {
    position: absolute;
    left: 268px;
    width: 648px;
    height: 360px;
    background: var(--cream);
    box-shadow: 5px 5px 4px var(--shadow);
    overflow: hidden;
  }
  .card--front { top: 54px; }
  .card--back { top: 446px; }

  .rule { position: absolute; left: 0; width: 100%; background: var(--teal); }

  /* front */
  .front__rule-top { top: 16px; height: 4px; }
  .front__dots {
    position: absolute; left: 6px; top: 22px; width: 636px; height: 11px;
    border-radius: 6px;
    background: var(--teal-soft);
  }
  .front__rule-dots { top: 36px; height: 2px; }
  .front__nameband { top: 45px; height: 44px; }
  .front__name {
    position: absolute; top: 44px; left: 0; width: 100%;
    text-align: center; font-weight: 700; font-size: 38px; letter-spacing: 0.5px;
    line-height: 44px;
  }
  .front__title {
    position: absolute; top: 86px; left: 0; width: 100%;
    text-align: center; font-weight: 500; font-size: 37px; line-height: 44px;
  }
  .front__phone {
    position: absolute; top: 128px; left: 0; width: 100%;
    text-align: center; font-weight: 500; font-size: 23px; line-height: 30px;
  }
  .front__brand {
    position: absolute; left: 250px; top: 162px; width: 144px; height: 144px;
    border-radius: 50%;
    background: var(--teal);
    display: flex; align-items: center; justify-content: center;
    text-align: center;
  }
  .front__brand-name {
    font-weight: 500; font-size: 19px; line-height: 22px; color: var(--navy);
    width: 110px;
  }
  .front__ornament {
    position: absolute; right: 0; top: 90px; width: 210px; height: 230px;
    background: radial-gradient(ellipse at 55% 40%, var(--teal) 0%, rgba(5,182,170,0.35) 55%, rgba(5,182,170,0) 75%);
  }
  .front__web {
    position: absolute; top: 303px; left: 0; width: 100%;
    text-align: center; font-weight: 500; font-size: 23px; line-height: 30px;
    white-space: nowrap;
  }
  .front__web span + span { margin-left: 12px; }
  .front__rule-bottom { top: 335px; height: 6px; }

  /* back */
  .back__rule-top { top: 21px; height: 8px; }
  .back__band { top: 73px; height: 195px; left: 1px; }
  .back__rule-bottom { top: 308px; height: 8px; }
  .gallery__item {
    position: absolute;
    border: 2px solid #e6ddc4;
  }
  .gallery__item--pottery {
    left: 139px; top: 115px; width: 112px; height: 111px;
    background: linear-gradient(180deg, #f4f4f2 0%, #3c8e6e 35%, #2f6f58 60%, #efe9e2 85%);
  }
  .gallery__item--jewelry {
    left: 264px; top: 117px; width: 110px; height: 105px;
    background: linear-gradient(180deg, #dcdcd8 0%, #c8c3bb 50%, #e47a86 70%, #d8d5cf 100%);
  }
  .gallery__item--bag {
    left: 387px; top: 113px; width: 112px; height: 113px;
    background: linear-gradient(90deg, #f3f1ee 0%, #b04a3a 40%, #3fc9b6 60%, #f3f1ee 100%);
  }
</style>
</head>
<body>
  <section class="card card--front" aria-label="Business card front">
    <div class="rule front__rule-top"></div>
    <div class="front__dots" role="img" aria-label="Row of small teal dots"></div>
    <div class="rule front__rule-dots"></div>
    <div class="rule front__nameband"></div>
    <h1 class="front__name">HELENA PIKEWORTH</h1>
    <p class="front__title">Designer</p>
    <p class="front__phone">phone 604.555.0172</p>
    <div class="front__brand">
      <span class="front__brand-name">Woven Glass and Tide</span>
    </div>
    <div class="front__ornament" role="img" aria-label="Teal floral vine ornament with blue flower centres"></div>
    <p class="front__web"><span>www.WovenGlassandTide.example</span><span>blog www.ShapingHillside.example</span></p>
    <div class="rule front__rule-bottom"></div>
  </section>

  <section class="card card--back" aria-label="Business card back">
    <div class="rule back__rule-top"></div>
    <div class="rule back__band"></div>
    <div class="gallery__item gallery__item--pottery" role="img" aria-label="Photo of a green glazed pottery vase"></div>
    <div class="gallery__item gallery__item--jewelry" role="img" aria-label="Photo of a pink braided necklace on a display bust"></div>
    <div class="gallery__item gallery__item--bag" role="img" aria-label="Photo of a turquoise and red leather bag"></div>
    <div class="rule back__rule-bottom"></div>
  </section>
</body>
</html>
```